Larkspur Ridge Management - Business Cards

I need business cards. My current logo was designed by a designer at this site and I very much like and am happy with the results. I would like a business card that is trendy, unique, current yet professional. I deal with high net worth clients daily

Target Market(s)

Out of state investors looking to get into the rental market in Ohio

Industry/Entity Type

Property Management, Consulting

Contact Information for Business Card

Name, Title (Chief Financial Officer) office phone number (555) 817-3094 website address larkridgemgmt.example

Font styles to use
Sans Serif

Colors
0054AA
0677BA
7BADD7
CADEEF
E8F1F8
0094D4
00A9DD
6FCCEA
C7EBF8
E9F6FB
00AB8E
00BBA5
67D7C9
C6EFE9
E9F9F6

```html
<!DOCTYPE html>
<html lang="en">
<head>
<meta charset="utf-8">
<title>Larkspur Ridge Management – Business Card</title>
<link href="https://fonts.googleapis.com/css2?family=Montserrat:wght@500;600;700&display=swap" rel="stylesheet">
<style>
  :root {
    --page-bg: #ffffff;
    --card-bg: #ffffff;
    --navy: #22355f;
    --red: #d0302f;
    --pattern-light: #f6f6f9;
    --pattern-dark: #e4e5ec;
  }
  * { box-sizing: border-box; margin: 0; padding: 0; }
  html, body {
    width: 992px;
    height: 1200px;
    overflow: hidden;
    background: var(--page-bg);
    font-family: "Montserrat", sans-serif;
  }
  .stage {
    position: relative;
    width: 992px;
    height: 1200px;
  }
  .business-card {
    position: absolute;
    left: 146px;
    top: 400px;
    width: 700px;
    height: 400px;
    background: var(--card-bg);
    box-shadow: 0 12px 18px rgba(0, 0, 0, 0.28);
    overflow: hidden;
  }
  .card-texture {
    position: absolute;
    inset: 0;
    background: linear-gradient(115deg, var(--pattern-dark) 0%, var(--pattern-light) 55%, var(--card-bg) 80%);
  }
  .brand-block {
    position: absolute;
    left: 40px;
    top: 150px;
    width: 250px;
    display: flex;
    align-items: center;
    gap: 12px;
  }
  .brand-mark {
    flex: 0 0 auto;
    width: 22px;
    height: 22px;
    border-radius: 50%;
    background: var(--navy);
  }
  .brand-name {
    font-size: 24px;
    font-weight: 700;
    line-height: 1.15;
    color: var(--navy);
  }
  .identity {
    position: absolute;
    right: 59px;
    top: 60px;
    text-align: right;
  }
  .person-name {
    font-size: 41px;
    font-weight: 700;
    color: var(--navy);
    line-height: 1;
  }
  .person-title {
    margin-top: 6px;
    font-size: 16px;
    font-weight: 600;
    letter-spacing: 1.1px;
    color: var(--red);
  }
  .contact-list {
    position: absolute;
    right: 59px;
    top: 254px;
    list-style: none;
    text-align: right;
    font-size: 19px;
    font-weight: 500;
    color: var(--navy);
    line-height: 31px;
  }
  .contact-list .accent { color: var(--red); }
</style>
</head>
<body>
<main class="stage">
  <section class="business-card">
    <div class="card-texture" role="img" aria-label="Faint repeating light grey background pattern"></div>

    <div class="brand-block">
      <span class="brand-mark"></span>
      <span class="brand-name">Larkspur Ridge Management</span>
    </div>

    <header class="identity">
      <h1 class="person-name">Daniel Hayes</h1>
      <p class="person-title">CHIEF FINANCIAL OFFICER</p>
    </header>

    <ul class="contact-list">
      <li>(555) 817-3094</li>
      <li>www.<span class="accent">larkridgemgmt</span>.example</li>
      <li>Maple Falls, Ohio 43999</li>
    </ul>
  </section>
</main>
</body>
</html>
```